Silver Hollow Dove Release Website Deisgn project

We need a website design for our dove release business.

We had several business cards designed awhile back....one for weddings and one for general releases (usually funerals). It was so hard to pick from all the great designs that were submitted. I have attached them.

We release white doves for all celebrations in life. Weddings, funerals, store openings, remembrance ceremonies, etc.

We need to appeal to brides and grooms as well as those grieving the loss of a loved one. It's a very delicate blend.

The name of our business is "Silver Hollow" and the name of our loft is "Marra's Roost". Our loft was established in 2012.

Target Market(s)

Brides, Grooms, Grieving Adults, Wedding Planners, Funeral Homes, Promoters

Industry/Entity Type

Professional Service

Number of Pages Required

5+ page

Font styles to use
Sans Serif

Requirements
Must have
• We will need some space for pictures I'm sure. We will need to have a contract & pricing page. We will need a contact us page.
• We need a more classic feel as we need to attract brides and those who are grieving. The solution may be a page for each......Wedding Releases & Funeral Releases & Other Celebrations
Nice to have
• If we have a page for each type of life celebration, there's more options for color. I would like the designer to choose the colors that are appropriate for the occasion.
• I would like to have a bit of decorative font in addition to the traditional website font.
Should not have
• We need to stay away from the yellow and orange colors.

```html
<!DOCTYPE html>
<html lang="en">
<head>
<meta charset="utf-8">
<title>Silver Hollow — White Dove Releases</title>
<link rel="stylesheet" href="https://fonts.googleapis.com/css2?family=Open+Sans:ital,wght@0,300;0,400;0,600;1,400&display=swap">
<style>
:root{
  --pink:#f46fb1;
  --ink:#2b2b2b;
  --text:#555;
  --panel:#f4f4f4;
  --card-border:#e6e6e6;
  --footer:#3a3a3a;
  --icon:#333;
  --white:#fff;
}
*{margin:0;padding:0;box-sizing:border-box}
html,body{width:1200px;height:2419px;overflow:hidden;background:var(--white)}
body{position:relative;font-family:"Open Sans",Arial,sans-serif;color:var(--ink)}
.abs{position:absolute}

/* header */
.site-header{left:0;top:0;width:1200px;height:231px;background:var(--white);border-bottom:1px solid #ddd}
.brand{left:0;width:1200px;top:42px;text-align:center;font-weight:300;font-size:52px;line-height:64px;letter-spacing:4px;color:#222}
.header-dove{left:1010px;top:22px;width:170px;height:170px;border-radius:6px;background:linear-gradient(160deg,#fafafa 0%,#ececec 55%,#f6f6f6 100%)}
.nav a{position:absolute;top:172px;font-size:16px;font-weight:300;color:#333;text-decoration:none;transform:translateX(-50%);white-space:nowrap;letter-spacing:.3px}
.nav-mark{left:241px;top:201px;width:24px;height:1px;background:#555}

/* hero */
.hero{left:0;top:231px;width:1200px;height:530px;background:linear-gradient(100deg,#5f8f36 0%,#a9c47d 25%,#e9e6e0 45%,#d7c2b6 60%,#3b3a45 78%,#6d9a44 100%)}
.hero-arrow{top:470px;width:14px;height:40px}

/* feature tabs */
.feature{top:695px;width:292px;height:139px;background:linear-gradient(#fafafa,#dedede);box-shadow:0 2px 5px rgba(0,0,0,.15)}
.feature.is-active{background:var(--pink)}
.feature h3{position:absolute;left:101px;top:34px;font-size:18px;font-weight:400;color:#333;letter-spacing:.3px}
.feature p{position:absolute;left:101px;top:69px;width:175px;font-size:10.5px;line-height:17px;color:#555}
.feature.is-active h3,.feature.is-active p{color:var(--white)}
.feature .icon{position:absolute;left:18px;top:42px;width:66px;height:60px}
.feature .icon-tile{position:absolute;left:28px;top:48px;width:46px;height:46px;border-radius:50%;background:var(--icon)}

/* welcome */
.welcome{left:0;top:761px;width:1200px;height:441px;background:var(--panel)}
.divider{width:194px;height:18px;left:503px}
.section-title{left:0;width:1200px;text-align:center;font-size:27px;font-weight:400;color:#222}
.intro{top:983px;width:310px;font-size:11px;line-height:18px;color:#555;text-align:justify}
.intro-photo{left:507px;top:956px;width:186px;height:186px;border-radius:50%;border:6px solid var(--white);box-shadow:0 0 0 1px #ccc;background:linear-gradient(160deg,#dfe6dc 0%,#7c9a58 55%,#3e5a2c 100%)}

/* celebration cards */
.card{width:281px;height:326px;background:var(--white);border:1px solid var(--card-border);box-shadow:0 1px 3px rgba(0,0,0,.06)}
.card-photo{left:0;top:0;width:279px;height:182px}
.card h3{position:absolute;left:0;width:279px;top:192px;text-align:center;font-size:20px;font-weight:400;color:#222}
.card .card-rule{position:absolute;left:16px;top:232px;width:247px;height:16px}
.card p{position:absolute;left:20px;width:239px;top:270px;text-align:center;font-size:11px;line-height:18px;color:#555}

/* testimonial */
.testimonial{left:0;top:2058px;width:1200px;height:208px;background:var(--pink)}
.quote{left:352px;top:2106px;width:686px;font-size:12px;line-height:19.5px;font-style:italic;color:var(--white);text-align:justify}
.quote b{font-size:22px;font-weight:600;line-height:0}
.quote-name{left:352px;top:2200px;font-size:12px;font-weight:600;color:var(--white)}

/* footer */
.site-footer{left:0;top:2266px;width:1200px;height:153px;background:var(--footer)}
.footer-links{left:0;width:1200px;top:2299px;text-align:center;font-size:10.5px;color:var(--white);letter-spacing:.3px}
.footer-links span{padding:0 7px}
.copyright{left:0;width:1200px;top:2327px;text-align:center;font-size:10.5px;color:#ddd}
.social{top:2364px;width:29px;height:29px;border:1.5px solid var(--white);border-radius:50%}
</style>
</head>
<body>

<header class="abs site-header">
  <div class="abs brand">Silver Hollow</div>
  <div class="abs header-dove" role="img" aria-label="White dove perched"></div>
  <nav class="nav">
    <a href="#" style="left:253px">HOME</a>
    <a href="#" style="left:397px">WEDDINGS</a>
    <a href="#" style="left:555px">FUNERALS</a>
    <a href="#" style="left:731px">SPECIAL EVENTS</a>
    <a href="#" style="left:919px">CONTACT US</a>
  </nav>
  <div class="abs nav-mark"></div>
</header>

<section class="abs hero" role="img" aria-label="Bride and groom releasing white doves in a garden"></section>
<svg class="abs hero-arrow" style="left:40px" viewBox="0 0 14 40"><path d="M12 2 2 20l10 18" fill="none" stroke="#fff" stroke-opacity=".6" stroke-width="1.5"/></svg>
<svg class="abs hero-arrow" style="left:1148px" viewBox="0 0 14 40"><path d="M2 2l10 18L2 38" fill="none" stroke="#fff" stroke-opacity=".6" stroke-width="1.5"/></svg>

<section class="abs welcome"></section>

<div class="abs feature" style="left:161px">
  <div class="icon-tile" role="img" aria-label="Dove icon"></div>
  <h3>FUNERALS</h3>
  <p>Sed ut perspiciatis unde omnis ist te natus error sit voluptatem.</p>
</div>
<div class="abs feature is-active" style="left:453px">
  <svg class="icon" viewBox="0 0 66 60"><circle cx="24" cy="36" r="15" fill="none" stroke="#fff" stroke-width="4"/><circle cx="42" cy="36" r="15" fill="none" stroke="#fff" stroke-width="4"/><path d="M24 14l4-5h-8z M42 14l4-5h-8z" fill="#fff"/></svg>
  <h3>WEDDINGS</h3>
  <p>Sed ut perspiciatis unde omnis ist te natus error sit voluptatem.</p>
</div>
<div class="abs feature" style="left:745px">
  <svg class="icon" viewBox="0 0 66 60"><path d="M22 50C8 38 4 30 4 23a9 9 0 0 1 18-3 9 9 0 0 1 18 3c0 7-4 15-18 27z" fill="#333"/><path d="M44 54C32 44 28 37 28 31a8 8 0 0 1 16-2 8 8 0 0 1 16 2c0 6-4 13-16 23z" fill="#333" stroke="#eee" stroke-width="2"/></svg>
  <h3>OUR EVENTS</h3>
  <p>Sed ut perspiciatis unde omnis ist te natus error sit voluptatem.</p>
</div>

<svg class="abs divider" style="top:883px" viewBox="0 0 194 18"><line x1="0" y1="9" x2="194" y2="9" stroke="#444"/><path d="M97 2l7 7-7 7-7-7z" fill="#f4f4f4" stroke="#444"/></svg>
<h2 class="abs section-title" style="top:905px">Welcome to Silver Hollow</h2>
<p class="abs intro" style="left:158px">Sed ut perspiciatis unde omnis iste natus error sit voluptatem accusantium doloremque laudantium, totam rem aperiam, eaque ipsa quae ab illo inventore veritatis et quasi architecto beatae vitae dicta sunt explicabo. Nemo enim ipsam voluptatem quia voluptas sit aspernatur aut odit aut fugit, sed quia consequuntur magni dolores eos qui ratione voluptatem sequi nesciunt. Neque porro quisquam est.</p>
<div class="abs intro-photo" role="img" aria-label="Outdoor wedding ceremony with a dove release"></div>
<p class="abs intro" style="left:732px">Sed ut perspiciatis unde omnis iste natus error sit voluptatem accusantium doloremque laudantium, totam rem aperiam, eaque ipsa quae ab illo inventore veritatis et quasi architecto beatae vitae dicta sunt explicabo. Nemo enim ipsam voluptatem quia voluptas sit aspernatur aut odit aut fugit, sed quia consequuntur magni dolores eos qui ratione voluptatem sequi nesciunt. Neque porro quisquam est.</p>

<svg class="abs divider" style="top:1233px" viewBox="0 0 194 18"><line x1="0" y1="9" x2="194" y2="9" stroke="#444"/><path d="M97 2l7 7-7 7-7-7z" fill="#fff" stroke="#444"/></svg>
<h2 class="abs section-title" style="top:1266px">Our White Doves Celebrations</h2>

<article class="abs card" style="left:161px;top:1328px">
  <div class="abs card-photo" role="img" aria-label="Wedding couple holding white doves" style="background:linear-gradient(90deg,#6b4a34,#d9d5d2 45%,#3a3f55 80%,#8b6a4a)"></div>
  <h3>Weddings</h3>
  <svg class="card-rule" viewBox="0 0 247 16"><line x1="4" y1="8" x2="243" y2="8" stroke="#333" stroke-width="1.5"/><path d="M123 2l6 6-6 6-6-6z M4 4l6 4-6 4z M243 4l-6 4 6 4z" fill="#fff" stroke="#333"/></svg>
  <p>Sed ut perspiciatis unde omnis iste natus error sit voluptatem accusantium doloremque laud</p>
</article>
<article class="abs card" style="left:460px;top:1328px">
  <div class="abs card-photo" role="img" aria-label="White rose held at a candlelit memorial" style="background:linear-gradient(90deg,#3d2a1e,#8a6d4e 35%,#e6e2d8 55%,#2a2522)"></div>
  <h3>Funerals</h3>
  <svg class="card-rule" viewBox="0 0 247 16"><line x1="4" y1="8" x2="243" y2="8" stroke="#333" stroke-width="1.5"/><path d="M123 2l6 6-6 6-6-6z M4 4l6 4-6 4z M243 4l-6 4 6 4z" fill="#fff" stroke="#333"/></svg>
  <p>Sed ut perspiciatis unde omnis iste natus error sit voluptatem accusantium doloremque laud</p>
</article>
<article class="abs card" style="left:758px;top:1328px">
  <div class="abs card-photo" role="img" aria-label="Ribbon cutting at a store opening" style="background:linear-gradient(135deg,#2e3440,#8e7e6c 40%,#c79d6a 55%,#6f7a88)"></div>
  <h3>Store Openings</h3>
  <svg class="card-rule" viewBox="0 0 247 16"><line x1="4" y1="8" x2="243" y2="8" stroke="#333" stroke-width="1.5"/><path d="M123 2l6 6-6 6-6-6z M4 4l6 4-6 4z M243 4l-6 4 6 4z" fill="#fff" stroke="#333"/></svg>
  <p>Sed ut perspiciatis unde omnis iste natus error sit voluptatem accusantium doloremque laud</p>
</article>

<article class="abs card" style="left:161px;top:1682px">
  <div class="abs card-photo" role="img" aria-label="Couple in formal wear holding doves" style="background:linear-gradient(90deg,#2a3550,#e8e4df 40%,#d8c9bd 70%,#f0ece8)"></div>
  <h3>Remembrance Ceremonies</h3>
  <svg class="card-rule" viewBox="0 0 247 16"><line x1="4" y1="8" x2="243" y2="8" stroke="#333" stroke-width="1.5"/><path d="M123 2l6 6-6 6-6-6z M4 4l6 4-6 4z M243 4l-6 4 6 4z" fill="#fff" stroke="#333"/></svg>
  <p>Sed ut perspiciatis unde omnis iste natus error sit voluptatem accusantium doloremque laud</p>
</article>
<article class="abs card" style="left:460px;top:1682px">
  <div class="abs card-photo" role="img" aria-label="Hands cradling a white dove" style="background:linear-gradient(90deg,#f1efec,#d9b8a5 40%,#efeeec 60%,#c9a08c)"></div>
  <h3>Celebrations &amp; Memorials</h3>
  <svg class="card-rule" viewBox="0 0 247 16"><line x1="4" y1="8" x2="243" y2="8" stroke="#333" stroke-width="1.5"/><path d="M123 2l6 6-6 6-6-6z M4 4l6 4-6 4z M243 4l-6 4 6 4z" fill="#fff" stroke="#333"/></svg>
  <p>Sed ut perspiciatis unde omnis iste natus error sit voluptatem accusantium doloremque laud</p>
</article>
<article class="abs card" style="left:758px;top:1682px">
  <div class="abs card-photo" role="img" aria-label="Child releasing a dove under a blue sky" style="background:linear-gradient(180deg,#4f86c6,#9cc3e8 60%,#c9d9b2)"></div>
  <h3>Other Celebrations</h3>
  <svg class="card-rule" viewBox="0 0 247 16"><line x1="4" y1="8" x2="243" y2="8" stroke="#333" stroke-width="1.5"/><path d="M123 2l6 6-6 6-6-6z M4 4l6 4-6 4z M243 4l-6 4 6 4z" fill="#fff" stroke="#333"/></svg>
  <p>Sed ut perspiciatis unde omnis iste natus error sit voluptatem accusantium doloremque laud</p>
</article>

<section class="abs testimonial"></section>
<svg class="abs" style="left:158px;top:2092px;width:176px;height:152px" viewBox="0 0 176 152" role="img" aria-label="Portrait of a bride holding a dove">
  <defs><linearGradient id="heartFill" x1="0" y1="0" x2="1" y2="1"><stop offset="0" stop-color="#e9d3c8"/><stop offset=".6" stop-color="#c9a494"/><stop offset="1" stop-color="#f2ece8"/></linearGradient></defs>
  <path d="M88 146C30 104 6 76 6 46A40 40 0 0 1 88 30a40 40 0 0 1 82 16c0 30-24 58-82 100z" fill="url(#heartFill)" stroke="#fff" stroke-width="5"/>
</svg>
<p class="abs quote"><b>“</b> Sed ut perspiciatis unde omnis iste natus error sit voluptatem accusantium doloremque laudantium, totam rem aperiam, eaque ipsa quae ab illo inventore veritatis et quasi architecto beatae vitae dicta sunt explicabo. Nemo enim ipsam voluptatem quia voluptas sit aspernatur aut odit aut fugit, sed quia consequuntur magni dolores eos qui ratione voluptatem sequi nesciunt. Neque porro quisquatur aut odit aut fugit, sed quia consequuntur magni dolores eos qui ratim est. <b>”</b></p>
<p class="abs quote-name">Clara Benton, City Name</p>

<footer class="abs site-footer"></footer>
<p class="abs footer-links"><span>HOME</span>|<span>WEDDINGS</span>|<span>FUNERALS</span>|<span>STORE OPENINGS</span>|<span>SPECIAL EVENTS</span>|<span>SERVICES</span>|<span>ABOUT US</span>|<span>CONTACT US</span></p>
<p class="abs copyright">© 2016 Silver Hollow All Copyrights Are Reserved. Terms of Use | Privacy Policy</p>
<div class="abs social" style="left:526px"></div>
<div class="abs social" style="left:563px"></div>
<div class="abs social" style="left:600px"></div>
<div class="abs social" style="left:641px"></div>

</body>
</html>
```